App-Design für Vergleichsportal für Reparaturen
Zielgruppe
Flickwerkstolz ist das Vergleichsportal für Reparaturen in deiner Nähe. Egal ob du eine Werkstatt für dein Smartphone, Tablet, Laptop, Computer, Smartwatch oder Spielkonsole suchst. Mit uns findest du deine passende Reparaturwerkstat in deiner Nähe mit dem besten Preis für dich. Du kannst dich direkt über unser Portal deinen Reparaturauftrag erhalten und wirst durch unser Lumen Kaufhut Käuferschutz und unser VORIBA Treuhandschutz abgesichert.
Aufgabenstellung
Unter Flickwerkstolz.de kann das aktuelle Design angeschaut werden. Die Farbe sollten übernommen werden.
Über die Startseite kann der Kunde sein Gerät, Service sowie seine Adresse eingeben. Auf der Vergleichsseite bekommt der Kunde die Übersicht welche Reparaturwerkstätten es gibt, zu welche Preisen die ausgewählte Dienstleistung angeboten wird. Wenn der Kunde auf den Button 'Jetzt Online Bestpreis buchen' drückt, dann kommt der Kunde in den Warenkorb. Im Warenkorb können noch weitere Dienstleistungen und Produkte dazugebucht werden. Und anschließend kommt der Kunde in die Kasse und kann der Bestellvorgang beenden. Die Benutzerführung sollte einfach sein. Im Fokus steht die Vergleichsseite. Dort sollte der Kunde ca. 4 Werkstätten auf einen Blick sehen können. Könnte ausschauen wie bei Preisluke7 in der Kategorie Mobilfunk.
Die Vergleichseite sollte auf jeden Fall folgende Elemente enthalten:
- Entfernung zur Werkstatt in Meter bzw. Kilometer
- Logo der Werkstatt
- Name der Werkstatt
- Bewertungssterne der Werkstatt
- Reparaturzeit und Ersatzeilverfügbarkeit
- Reparaturpreis (Platz sollte auch bei Auswahl von 2 Dienstleistungen vorhanden sein)
- Rabattanzeige
- Qualitätssiegel (noch nicht vorhanden)
- Anzeige von Verknappung (z. B. noch 3 Termin frei)
- Qualitätsmerkmale (z. B. 12 Monate Garantie)
Die Merkmale Öffnungszeiten, Adresse, Kostenpflichtige Zusatzleistungen können aus Platzgründen in den Warenkorbseite wandern außer es gibt eine schöne und einfache Lösung.
In der Warenkorbseite kann dazu auch die Preisluke7 Seite dienen.
Bei allen sollte auf die Benutzerfreundlichkeit geachtet werden.
Bei offenen Frage stehe ich zur Verfügung und freue mich auf viele Designs.
Vielen DANK im Voraus!

```html
<!DOCTYPE html>
<html lang="de">
<head>
<meta charset="utf-8">
<title>Flickwerkstolz – App-Screens</title>
<link href="https://fonts.googleapis.com/css2?family=Inter:wght@400;500;600;700&display=swap" rel="stylesheet">
<style>
:root{
  --bg:#f7f7f7;
  --panel:#efefef;
  --white:#ffffff;
  --ink:#1d1d1d;
  --muted:#8a8a8a;
  --line:#e4e4e4;
  --teal:#1f4459;
  --green:#8cc63f;
  --green-dark:#6fa82c;
  --grey-btn:#c9c9c9;
  --star-off:#d6d6d6;
}
*{box-sizing:border-box;margin:0;padding:0}
html,body{width:1200px;height:993px;overflow:hidden;background:var(--bg)}
body{font-family:"Inter",Helvetica,Arial,sans-serif;color:var(--ink)}
.board{position:absolute;left:0;top:0;width:1428px;height:1182px;transform:scale(0.8403);transform-origin:0 0}
.screen{position:absolute;width:287px;height:510px;background:var(--white);box-shadow:0 1px 4px rgba(0,0,0,.25);overflow:hidden}
.abs{position:absolute}
.status{position:absolute;left:0;top:0;width:100%;height:18px;padding:0 5px;display:flex;justify-content:space-between;align-items:center;font-size:8px}
.batt{display:inline-block;width:17px;height:7px;background:var(--ink);vertical-align:-1px;margin-left:2px}
.appbar{position:absolute;left:0;top:18px;width:100%;height:44px}
.brand{position:absolute;left:50%;top:12px;transform:translateX(-50%);display:flex;align-items:center;gap:4px;font-size:10px;font-weight:600;color:var(--green-dark);white-space:nowrap}
.brand i{width:12px;height:12px;border-radius:50%;background:var(--teal);display:block}
.back{position:absolute;left:20px;top:14px;width:12px;height:16px}
.basket{position:absolute;right:20px;top:14px;width:20px;height:16px}
.count{position:absolute;right:16px;top:10px;font-size:7px;font-weight:600}
.section{position:absolute;left:0;top:62px;width:100%;height:28px;background:var(--panel);font-size:8px;font-weight:500;letter-spacing:.3px;text-align:center;line-height:28px;text-transform:uppercase}
.grey{position:absolute;left:0;width:100%;background:var(--panel)}
.cta{position:absolute;left:0;bottom:0;width:100%;height:49px;background:var(--teal);color:var(--white);font-size:10px;font-weight:600;letter-spacing:.5px;text-align:center;line-height:49px;text-transform:uppercase}
.cta.disabled{background:var(--grey-btn)}
.row{position:absolute;left:0;width:100%;background:var(--white);border-bottom:1px solid var(--line);display:flex;align-items:center;padding:0 33px;font-size:10px;font-weight:500}
.row .chev{margin-left:auto;font-size:11px}
.dots{position:absolute;left:0;width:100%;text-align:center;font-size:0}
.dots span{display:inline-block;width:3px;height:3px;border-radius:50%;background:#c8c8c8;margin:0 2px}
.dots span.on{background:var(--muted)}
.device{position:absolute;top:108px;width:102px;height:95px;background:var(--white);border-radius:3px;font-size:9px;text-align:center}
.device.active{border:2px solid var(--green)}
.device svg{display:block;margin:18px auto 8px}
.shop-card{position:absolute;width:121px;height:158px;background:var(--white);border-radius:3px;padding:0 9px}
.shop-card.active{border:2px solid var(--green)}
.shop-mark{position:absolute;font-size:5px;font-weight:700;color:var(--green-dark)}
.shop-mark::before{content:"";position:absolute;left:26px;top:-4px;width:28px;height:3px;border-top:1px solid var(--green)}
.seal{position:absolute;border-radius:50%;background:#6a6a6a;border:2px solid #e0e0e0}
.shop-card .name{position:absolute;left:9px;top:38px;font-size:10px;font-weight:700;line-height:13px}
.shop-card .addr{position:absolute;left:9px;top:75px;font-size:6.5px;line-height:9.5px;color:#444}
.shop-card .feat{position:absolute;left:9px;top:116px;font-size:7px;color:#333}
.shop-card .stats{position:absolute;left:9px;right:9px;top:129px;display:flex;justify-content:space-between}
.stat small{display:block;font-size:4px;color:var(--muted);margin-bottom:3px}
.stat b{font-size:8px;font-weight:600}
.slot{position:absolute;width:61px;height:30px;border:1px solid var(--line);border-radius:2px;font-size:10px;text-align:center;line-height:28px;color:#444}
.slot.on{background:var(--green);border-color:var(--green);color:var(--white);font-weight:600}
.cart-row{position:absolute;left:0;width:100%;background:var(--white);border-bottom:1px solid var(--line);display:flex;align-items:center;padding:0 33px 0 33px;font-size:9.5px}
.cart-row .x{color:var(--muted);margin-right:10px;font-size:9px}
.cart-row .price{margin-left:auto;font-weight:600}
.cart-row .price small{font-size:4.5px;color:var(--muted);font-weight:400;margin-right:3px}
.total{position:absolute;left:0;width:100%;background:var(--green);color:var(--white);display:flex;align-items:center;padding:0 33px 0 36px;font-size:10px;font-weight:600}
.total span:last-child{margin-left:auto}
.extra{position:absolute;left:0;width:100%;height:34px;background:var(--white);border-bottom:1px solid var(--line);display:flex;align-items:center;padding:0 24px 0 33px;font-size:10px}
.extra svg{margin-right:8px}
.extra .info{margin-left:auto;width:7px;height:7px;border-radius:50%;background:#cfcfcf}
.pay{position:absolute;top:318px;height:22px;background:var(--white);font-size:11px;font-weight:700;color:var(--teal);text-align:center;line-height:22px}
.pay.on{border:2px solid var(--green);line-height:18px}
.center-text{position:absolute;left:0;width:100%;text-align:center}
</style>
</head>
<body>
<svg width="0" height="0" style="position:absolute" aria-hidden="true">
  <symbol id="i-basket" viewBox="0 0 20 16"><path d="M1 6h18l-2.5 9h-13z M5 6l4-5 M15 6l-4-5" fill="none" stroke="#1d1d1d" stroke-width="1.6" stroke-linejoin="round"/></symbol>
  <symbol id="i-back" viewBox="0 0 12 16"><path d="M9 2L3 8l6 6" fill="none" stroke="#1d1d1d" stroke-width="2"/></symbol>
  <symbol id="i-signal" viewBox="0 0 8 8"><path d="M4 7V2 M2 3l2-2 2 2" fill="none" stroke="#1d1d1d" stroke-width="1.2"/></symbol>
  <symbol id="i-phone" viewBox="0 0 8 8"><path d="M1.5 1l1.7-.2 1 2-1 .8a4 4 0 0 0 1.7 1.7l.8-1 2 1-.2 1.7C5 7.4 .6 3 1.5 1z" fill="#8cc63f"/></symbol>
  <symbol id="i-pin" viewBox="0 0 8 10"><path d="M4 9.5S.8 5.8.8 3.6a3.2 3.2 0 0 1 6.4 0C7.2 5.8 4 9.5 4 9.5z" fill="#1d1d1d"/><circle cx="4" cy="3.6" r="1.1" fill="#fff"/></symbol>
  <symbol id="i-wifi" viewBox="0 0 10 8"><path d="M1 3a6 6 0 0 1 8 0 M2.6 4.6a3.6 3.6 0 0 1 4.8 0" fill="none" stroke="#1d1d1d" stroke-width="1.1"/><circle cx="5" cy="6.6" r=".9" fill="#1d1d1d"/></symbol>
  <symbol id="i-wrench" viewBox="0 0 10 10"><path d="M1 9l4.5-4.5 M6 1.2a2.4 2.4 0 0 0 2.8 2.8L7.6 5.2 4.8 2.4z" fill="none" stroke="#1d1d1d" stroke-width="1.4"/></symbol>
  <symbol id="i-star" viewBox="0 0 10 10"><path d="M5 .5l1.4 2.9 3.1.4-2.3 2.2.6 3.1L5 7.6 2.2 9.1l.6-3.1L.5 3.8l3.1-.4z"/></symbol>
</svg>

<main class="board">

  <!-- Startbildschirm -->
  <section class="screen" style="left:56px;top:62px">
    <div class="status"><span>●●●●● Netz</span><span>9:41 AM</span><span>100% <i class="batt"></i></span></div>
    <div class="abs" style="left:0;top:158px;width:100%;display:flex;justify-content:center;align-items:center;gap:10px">
      <i style="display:block;width:30px;height:30px;border-radius:50%;background:var(--green)"></i>
      <span style="font-size:30px;font-weight:500;color:var(--teal);letter-spacing:.3px">flickwerkstolz</span>
    </div>
    <p class="center-text" style="top:398px;font-size:11.5px;font-weight:700;line-height:16px">DAS VERGLEICHSPORTAL FÜR<br>REPARATUREN IN DEINER NÄHE</p>
    <div class="abs" style="left:0;bottom:0;width:100%;height:12px;border-top:1px solid var(--line);font-size:4.5px;color:var(--muted);text-align:center;line-height:11px">Datenschutz</div>
  </section>

  <!-- Reparaturangaben -->
  <section class="screen" style="left:384px;top:62px">
    <div class="status"><span>●●●●● Netz</span><span>9:41 AM</span><span>100% <i class="batt"></i></span></div>
    <header class="appbar"><div class="brand"><i></i>flickwerkstolz</div><svg class="basket"><use href="#i-basket"/></svg></header>
    <div class="section">Reparaturangaben</div>
    <div class="grey" style="top:90px;height:148px"></div>
    <div class="device" style="left:-88px;width:102px"><svg width="14" height="38" viewBox="0 0 14 38" style="margin:18px 0 0 84px"><rect x="1" y="1" width="12" height="36" rx="2" fill="none" stroke="#1d1d1d" stroke-width="2"/></svg></div>
    <div class="device active" style="left:35px"><svg width="30" height="38" viewBox="0 0 30 38"><rect x="1" y="1" width="28" height="36" rx="3" fill="none" stroke="#1d1d1d" stroke-width="2"/><line x1="12" y1="32" x2="18" y2="32" stroke="#1d1d1d" stroke-width="1.5"/></svg>Tablet</div>
    <div class="device" style="left:145px"><svg width="46" height="30" viewBox="0 0 46 30" style="margin-top:26px"><rect x="3" y="1" width="40" height="25" fill="none" stroke="#1d1d1d" stroke-width="1.8"/><line x1="0" y1="28.5" x2="46" y2="28.5" stroke="#1d1d1d" stroke-width="1.8"/></svg>Laptop</div>
    <div class="device" style="left:255px"></div>
    <div class="dots" style="top:214px"><span></span><span class="on"></span><span></span><span></span><span></span></div>
    <div class="row" style="top:238px;height:38px">Hersteller wählen<span class="chev">›</span></div>
    <div class="row" style="top:276px;height:37px">Dienstleistung wählen<span class="chev">›</span></div>
    <div class="section" style="top:313px;height:38px;line-height:38px;font-size:7.5px">Geben Sie Ihre Agresse ein</div>
    <div class="row" style="top:351px;height:37px">Strasse</div>
    <div class="row" style="top:388px;height:37px">Hausnummer</div>
    <div class="grey" style="top:425px;height:36px"></div>
    <div class="cta">Los</div>
  </section>

  <!-- Standorte: Vergleich -->
  <section class="screen" style="left:715px;top:62px">
    <div class="status"><span>●●●●● Netz</span><span>9:41 AM</span><span>100% <i class="batt"></i></span></div>
    <header class="appbar"><svg class="back"><use href="#i-back"/></svg><div class="brand"><i></i>flickwerkstolz</div><svg class="basket"><use href="#i-basket"/></svg><span class="count">3</span></header>
    <div class="section">Standorte in der Nähe</div>
    <div class="grey" style="top:90px;height:371px"></div>

    <article class="shop-card active" style="left:18px;top:107px">
      <span class="shop-mark" style="left:8px;top:25px">zellwerk.de</span>
      <span class="seal" style="left:90px;top:9px;width:22px;height:22px" role="img" aria-label="Qualitätssiegel"></span>
      <h3 class="name">Zellwerk<br>Lumen Kaufhut</h3>
      <p class="addr">Lindenhofstr. 14<br>89217 Altwiesen</p>
      <p class="feat"><svg width="7" height="7" style="vertical-align:-1px"><use href="#i-signal"/></svg> Funk Antenne</p>
      <div class="stats"><div class="stat"><small>Preis -50%</small><b>100 €</b></div><div class="stat"><small>Garantie</small><b>12 Mo.</b></div><div class="stat"><small>Reparatur</small><b>4 St.</b></div></div>
    </article>
    <article class="shop-card" style="left:148px;top:107px">
      <span class="shop-mark" style="left:9px;top:27px">zellwerk.de</span>
      <h3 class="name">Zellwerk<br>Lumen Kaufhut</h3>
      <p class="addr">Lindenhofstr. 14<br>89217 Altwiesen</p>
      <p class="feat"><svg width="7" height="7" style="vertical-align:-1px"><use href="#i-signal"/></svg> Funk Antenne</p>
      <div class="stats"><div class="stat"><small>Preis</small><b>100 €</b></div><div class="stat"><small>Garantie</small><b>12 Mo.</b></div><div class="stat"><small>Reparatur</small><b>4 St.</b></div></div>
    </article>
    <article class="shop-card" style="left:18px;top:273px">
      <span class="shop-mark" style="left:9px;top:25px">zellwerk.de</span>
      <h3 class="name">Zellwerk<br>Lumen Kaufhut</h3>
      <p class="addr">Lindenhofstr. 14<br>89217 Altwiesen</p>
      <p class="feat"><svg width="7" height="7" style="vertical-align:-1px"><use href="#i-signal"/></svg> Funk Antenne</p>
      <div class="stats"><div class="stat"><small>Preis</small><b>100 €</b></div><div class="stat"><small>Garantie</small><b>12 Mo.</b></div><div class="stat"><small>Reparatur</small><b>4 St.</b></div></div>
    </article>
    <article class="shop-card" style="left:148px;top:273px">
      <span class="shop-mark" style="left:9px;top:25px">zellwerk.de</span>
      <span class="seal" style="left:92px;top:9px;width:22px;height:22px" role="img" aria-label="Qualitätssiegel"></span>
      <h3 class="name">Zellwerk<br>Lumen Kaufhut</h3>
      <p class="addr">Lindenhofstr. 14<br>89217 Altwiesen</p>
      <p class="feat"><svg width="7" height="7" style="vertical-align:-1px"><use href="#i-signal"/></svg> Funk Antenne</p>
      <div class="stats"><div class="stat"><small>Preis</small><b>100 €</b></div><div class="stat"><small>Garantie</small><b>12 Mo.</b></div><div class="stat"><small>Reparatur</small><b>4 St.</b></div></div>
    </article>
    <div class="dots" style="top:441px"><span></span><span class="on"></span><span></span><span></span><span></span></div>
    <div class="cta">Jetzt online Bestpreis buchen</div>
  </section>

  <!-- Standort-Details -->
  <section class="screen" style="left:1056px;top:62px">
    <div class="status"><span>●●●●● Netz</span><span>9:41 AM</span><span>100% <i class="batt"></i></span></div>
    <header class="appbar"><svg class="back"><use href="#i-back"/></svg><div class="brand"><i></i>flickwerkstolz</div><svg class="basket"><use href="#i-basket"/></svg><span class="count">3</span></header>
    <div class="section">Standorte in der Nähe</div>
    <div class="grey" style="top:90px;height:371px"></div>
    <article class="abs" style="left:17px;top:111px;width:253px;height:250px;background:var(--white);border-radius:3px">
      <span class="shop-mark" style="left:19px;top:31px;font-size:6px">zellwerk.de</span>
      <span class="seal" style="left:211px;top:-9px;width:46px;height:46px" role="img" aria-label="Qualitätssiegel"></span>
      <h2 class="abs" style="left:19px;top:48px;font-size:16px;font-weight:700">Zellwerk Go GmbH</h2>
      <p class="abs" style="left:19px;top:80px;font-size:10px;line-height:14px;color:#333">Lindenhofstr. 14<br>89217 Altwiesen</p>
      <p class="abs" style="left:19px;top:111px;font-size:5.5px;color:var(--muted)">Auf Karte</p>
      <p class="abs" style="left:19px;top:140px;font-size:8.5px;line-height:15px"><svg width="8" height="8"><use href="#i-phone"/></svg> 04512 - 3308 740<br><svg width="8" height="8"><use href="#i-phone"/></svg> 04512 - 6691 208</p>
      <p class="abs" style="right:19px;top:140px;font-size:8.5px;line-height:15px;text-align:right">Mo-Fr. 9.00 - 18.00 Uhr<br>Sa. 10.00 - 15.00 Uhr</p>
      <p class="abs" style="left:33px;top:188px;font-size:25px;font-weight:700">150 <span style="font-size:17px;font-weight:500">m.</span></p>
      <div class="abs" style="left:33px;top:220px;display:flex;gap:2px;fill:var(--green)">
        <svg width="11" height="11"><use href="#i-star"/></svg><svg width="11" height="11"><use href="#i-star"/></svg><svg width="11" height="11"><use href="#i-star"/></svg><svg width="11" height="11"><use href="#i-star"/></svg><svg width="11" height="11" style="fill:var(--star-off)"><use href="#i-star"/></svg>
      </div>
      <svg class="abs" style="left:175px;top:189px" width="26" height="24" viewBox="0 0 26 24"><rect x="1.5" y="3.5" width="23" height="19" fill="none" stroke="#1d1d1d" stroke-width="1.8"/><rect x="1.5" y="3.5" width="23" height="4" fill="#1d1d1d"/><line x1="7" y1="0" x2="7" y2="5" stroke="#1d1d1d" stroke-width="1.8"/><line x1="19" y1="0" x2="19" y2="5" stroke="#1d1d1d" stroke-width="1.8"/><text x="13" y="19.5" text-anchor="middle" font-size="10" font-weight="700" font-family="Inter,sans-serif">19</text></svg>
      <p class="abs" style="left:160px;top:222px;font-size:5px;color:var(--muted)">noch <b style="font-size:8px;color:var(--ink)">3</b> Termin frei</p>
    </article>
    <div class="cart-row" style="top:373px;height:40px;padding:0 35px 0 19px"><span class="x">✕</span>Funk Antenne<span class="price" style="text-align:right;line-height:10px">100 €<br><small style="font-size:5px;margin:0">Garantie 12 Monate</small></span></div>
    <div class="cart-row" style="top:420px;height:41px;padding:0 35px 0 19px"><span class="x">✕</span>SIM Lesemodul<span class="price" style="text-align:right;line-height:10px">100 €<br><small style="font-size:5px;margin:0">Garantie 24 Monate</small></span></div>
    <div class="cta">Zur Kasse</div>
  </section>

  <!-- Terminauswahl -->
  <section class="screen" style="left:384px;top:621px">
    <div class="status"><span>●●●●● Netz</span><span>9:41 AM</span><span>100% <i class="batt"></i></span></div>
    <header class="appbar"><svg class="back"><use href="#i-back"/></svg><div class="brand"><i></i>flickwerkstolz</div><svg class="basket"><use href="#i-basket"/></svg><span class="count">3</span></header>
    <div class="section" style="height:20px;line-height:28px;background:var(--white)">Standorte in der Nähe</div>
    <div class="grey" style="top:430px;height:31px"></div>
    <div class="abs" style="left:16px;top:83px;width:257px;height:334px;background:var(--white);border:2px solid var(--green)">
      <h3 class="abs" style="left:18px;top:16px;font-size:10px;font-weight:700">Nächste Termine</h3>
      <svg class="abs" style="left:226px;top:15px" width="12" height="12"><path d="M1 1l10 10M11 1L1 11" stroke="#aaa" stroke-width="1.2"/></svg>
      <p class="abs" style="left:18px;top:48px;font-size:9px">AUG 17</p>
      <span class="slot on" style="left:18px;top:64px">11 AM</span>
      <span class="slot" style="left:91px;top:64px">1 PM</span>
      <span class="slot" style="left:165px;top:64px">3 PM</span>
      <span class="slot" style="left:18px;top:107px">4 PM</span>
      <span class="slot" style="left:91px;top:107px">11 AM</span>
      <p class="abs" style="left:18px;top:158px;font-size:9px">AUG 19</p>
      <span class="slot" style="left:18px;top:174px">10 AM</span>
      <span class="slot" style="left:91px;top:174px">11 AM</span>
      <p class="abs" style="left:16px;top:235px;font-size:8.5px;text-decoration:underline">SHOW CALENDAR</p>
      <div class="abs" style="left:16px;top:276px;width:217px;height:36px;border-radius:4px;background:var(--teal);color:var(--white);font-size:10px;font-weight:600;letter-spacing:.4px;text-align:center;line-height:36px">TERMIN BUCHEN</div>
    </div>
    <div class="cta disabled">Zur Kasse</div>
  </section>

  <!-- Warenkorb -->
  <section class="screen" style="left:715px;top:621px">
    <div class="status"><span>●●●●● Netz</span><span>9:41 AM</span><span>100% <i class="batt"></i></span></div>
    <header class="appbar"><svg class="back"><use href="#i-back"/></svg><div class="brand"><i></i>flickwerkstolz</div><svg class="basket"><use href="#i-basket"/></svg><span class="count">3</span></header>
    <div class="section">Warenkorb</div>
    <div class="abs" style="left:0;top:90px;width:100%;height:30px;background:#f4f4f4;display:flex;align-items:center;justify-content:space-between;padding:0 38px 0 50px;font-size:8.5px;color:var(--muted)"><span>Leistung</span><span>Preis</span></div>
    <div class="cart-row" style="top:120px;height:34px"><span class="x">✕</span>Funk Antenne<span class="price"><small>200€ -50%</small>100 €</span></div>
    <div class="cart-row" style="top:154px;height:34px"><span class="x">✕</span>SIM Lesemodul<span class="price">100 €</span></div>
    <div class="total" style="top:188px;height:35px"><span>Total</span><span>200 €</span></div>
    <div class="section" style="top:223px;height:67px;line-height:110px;font-size:7.5px">Zusätzliche Leistungen</div>
    <div class="extra" style="top:290px"><svg width="7" height="9"><use href="#i-pin"/></svg>W-LAN Antenne<i class="info"></i></div>
    <div class="extra" style="top:324px"><svg width="9" height="8"><use href="#i-wifi"/></svg>GPS Antenne<i class="info"></i></div>
    <div class="extra" style="top:358px"><svg width="7" height="9"><use href="#i-pin"/></svg>W-LAN Antenne<i class="info"></i></div>
    <div class="extra" style="top:392px"><svg width="8" height="8"><use href="#i-signal"/></svg>Funk Antenne<i class="info"></i></div>
    <div class="extra" style="top:426px"><svg width="8" height="8"><use href="#i-wrench"/></svg>SIM Lesemodul<i class="info"></i></div>
    <div class="cta">Bezahlen</div>
  </section>

  <!-- Checkout -->
  <section class="screen" style="left:1056px;top:621px">
    <div class="status"><span>●●●●● Netz</span><span>9:41 AM</span><span>100% <i class="batt"></i></span></div>
    <header class="appbar"><svg class="back"><use href="#i-back"/></svg><div class="brand"><i></i>flickwerkstolz</div><svg class="basket"><use href="#i-basket"/></svg><span class="count">3</span></header>
    <div class="section">Checkout</div>
    <div class="grey" style="top:90px;height:265px"></div>
    <h2 class="center-text" style="top:115px;font-size:21px;font-weight:700;color:var(--teal)">Vielen Dank!</h2>
    <span class="shop-mark" style="left:106px;top:170px;font-size:6px">zellwerk.de</span>
    <p class="center-text" style="top:194px;font-size:9px;line-height:14px">Lindenhofstr. 14<br>89217 Altwiesen</p>
    <p class="center-text" style="top:232px;font-size:9px;line-height:14px">Öffnungszeiten:<br>Mo-Fr. 9.00 Uhr - 18.00 Uhr<br>Sa. 10.00 Uhr - 15.00 Uhr</p>
    <p class="center-text" style="top:298px;font-size:9.5px">Zahlungsmethoden:</p>
    <div class="pay on" style="left:36px;width:63px;">Kartaro</div>
    <div class="pay" style="left:107px;width:77px">Zahlfix</div>
    <div class="pay" style="left:191px;width:62px;font-size:10px;color:var(--ink)">Ratenly</div>
    <div class="cart-row" style="top:355px;height:37px"><span>Funk Antenne</span><span class="price"><small>200€ -50%</small>100 €</span></div>
    <div class="cart-row" style="top:392px;height:36px"><span>SIM Lesemodul</span><span class="price">100 €</span></div>
    <div class="total" style="top:428px;height:33px"><span>Total</span><span>200 €</span></div>
    <div class="cta">Bezahlen</div>
  </section>

</main>
</body>
</html>
```